Vellart

I already have a website created through Makrive.com - https://vellart.co.nz.

Its an accounting services business, can get ideas from wexo.co.nz, fyn.co.nz, hul.co.nz

I would like to have this recreated using coding. I need the following features and functionalities incorporated:

- Live Chat feature
- Moving Carousel feature for Reviews
- Advanced SEO support (Google Analytics)

Industry/Entity Type

accounting

Coding

Coded - Design and coding required

Number of Pages Required

5+ page

```html
<!DOCTYPE html>
<html lang="en">
<head>
<meta charset="utf-8">
<title>Vellart — Accounting for Small Businesses</title>
<link rel="stylesheet" href="https://fonts.googleapis.com/css2?family=Lexend:wght@400;500;600&family=Inter:wght@400;500;600&display=swap">
<style>
:root{
  --ink:#111b19;
  --text:#2b3533;
  --muted:#5d6664;
  --teal:#5cbfa3;
  --teal-deep:#1d6f5b;
  --mint:#acd9cc;
  --mint-soft:#d3ebe4;
  --slate:#3c4947;
  --panel:#f6f7f7;
  --footer:#3fa68e;
  --white:#ffffff;
}
*{box-sizing:border-box;margin:0;padding:0}
html,body{width:1200px;height:3987px;overflow:hidden;background:var(--white)}
body{position:relative;font-family:'Inter',sans-serif;color:var(--text)}
.abs{position:absolute}
h1,h2,h3,.display{font-family:'Lexend',sans-serif;font-weight:500;color:var(--ink)}
.lede{font-size:11.5px;line-height:16px;color:var(--muted)}
.photo{border-radius:8px}

/* buttons */
.cta{position:absolute;display:flex;align-items:center;height:46px;border-radius:23px;
  background:linear-gradient(90deg,#050a09 0%,#0d3a30 60%,var(--teal-deep) 100%);color:#fff;font-size:14px;padding-left:16px}
.cta .cta-arrow{position:absolute;right:-2px;top:-1px;width:48px;height:48px;border-radius:50%;background:#fff;
  display:flex;align-items:center;justify-content:center;box-shadow:0 2px 6px rgba(0,0,0,.12)}

/* header */
.site-header{position:absolute;left:0;top:0;width:1200px;height:135px;border-bottom:1px solid #e4e7e6}
.brand{position:absolute;left:88px;top:62px;display:flex;align-items:center;gap:8px;font-family:'Lexend',sans-serif;
  font-weight:500;font-size:20px;letter-spacing:4px;color:var(--teal)}
.brand-dot{width:14px;height:14px;border-radius:50%;background:var(--teal)}
.nav a{position:absolute;top:64px;font-size:13.5px;color:var(--ink);text-decoration:none}
.nav a.active{color:var(--teal-deep)}

/* hero */
.hero-title{left:82px;top:262px;font-size:46px;line-height:58px}
.hero-photo{left:700px;top:196px;width:452px;height:472px;border-radius:24px;background:linear-gradient(160deg,#e6e6e6,#cdcdcd)}
.tax-card{left:551px;top:333px;width:279px;height:178px;background:#fff;border-radius:10px;box-shadow:0 6px 24px rgba(0,0,0,.08)}
.partners span{position:absolute;top:718px;font-family:'Lexend',sans-serif;font-size:26px;font-weight:500;color:#9aa09f;display:flex;align-items:center;gap:8px}
.partners i{display:inline-block;width:26px;height:26px;border-radius:50%;background:#a8adac}

/* about */
.feature-icon{position:absolute;width:56px;height:56px;border-radius:6px;background:var(--mint);display:flex;align-items:center;justify-content:center}
.feature-title{position:absolute;font-size:14px;color:var(--ink)}
.feature-text{position:absolute;font-size:11px;line-height:14px;color:var(--text)}

/* services */
.services-band{left:0;top:1378px;width:1200px;height:511px;background:var(--mint)}
.service-card{position:absolute;top:1667px;width:247px;height:177px;background:#fff;border-radius:6px;padding:18px 16px}
.service-card.dark{background:var(--slate);color:#fff}
.service-card .ico{width:46px;height:40px;border-radius:6px;background:var(--mint);margin-bottom:16px;display:flex;align-items:center;justify-content:center}
.service-card.dark .ico{background:#fff}
.service-card h3{font-family:'Inter',sans-serif;font-weight:500;font-size:14px;color:inherit;margin-bottom:12px}
.service-card p{font-size:11px;line-height:16px;color:#555}
.service-card.dark p{color:#e6ecea}

/* pricing */
.plan{position:absolute;left:607px;width:483px;height:177px;background:var(--mint-soft);border:2px solid #c4dcd5;border-radius:10px;box-shadow:0 3px 8px rgba(0,0,0,.08)}
.plan .price{position:absolute;left:28px;top:26px;font-size:14px;font-weight:600;color:var(--ink)}
.plan .price small{font-size:8px;font-weight:400}
.plan .tier{position:absolute;left:32px;top:52px;font-size:12px;color:var(--ink)}
.plan .who{position:absolute;left:28px;top:78px;font-size:13px;line-height:22px;color:var(--ink)}
.plan ul{position:absolute;left:280px;top:24px;list-style:none;font-size:13px;line-height:34px;color:var(--ink)}
.plan li:before{content:"•";margin-right:4px}
.plan-badge{position:absolute;height:27px;padding:0 14px;border-radius:8px;background:linear-gradient(90deg,#0a1714,var(--teal-deep));color:#fff;font-size:12.5px;line-height:27px}
.plan-list div{position:absolute;left:113px;font-size:18px;color:var(--ink)}

/* faq */
.center{left:0;width:1200px;text-align:center}
.rule{position:absolute;left:291px;width:616px;height:1px;background:#b8bfbd}

/* contact */
.form-panel{left:229px;top:3008px;width:457px;height:450px;background:var(--panel);border-radius:6px}
.field-label{position:absolute;font-size:12px;color:var(--ink)}
.field{position:absolute;background:#fff;border:1.5px solid #cfd3d2;border-radius:5px}
.info-panel{left:700px;top:3025px;width:271px;height:419px;background:var(--mint)}
.info-panel .row{position:absolute;left:19px;display:flex;align-items:center;gap:10px;font-size:13px;color:#fff}

/* footer */
.site-footer{left:0;top:3557px;width:1200px;height:430px;background:linear-gradient(120deg,#3a9c85 0%,var(--footer) 50%,#58b79e 100%)}
.site-footer a,.site-footer .f{position:absolute;font-size:14px;color:#fff;text-decoration:none}
.foot-rule{position:absolute;left:0;width:1200px;height:1px;background:rgba(255,255,255,.55)}
</style>
</head>
<body>

<header class="site-header">
  <div class="brand"><span class="brand-dot"></span>VELLART</div>
  <nav class="nav">
    <a class="active" style="left:356px">Home</a>
    <a style="left:450px">About Us</a>
    <a style="left:562px">Services</a>
    <a style="left:670px">Pricing</a>
    <a style="left:769px">Faqs</a>
  </nav>
  <div class="cta" style="left:932px;top:49px;width:206px;height:45px;font-size:13px;border-radius:8px 23px 23px 8px">Book an Appointment
    <span class="cta-arrow" style="width:46px;height:46px"><svg width="18" height="18" viewBox="0 0 18 18"><path d="M4 14L14 4M6 4h8v8" stroke="#1d6f5b" stroke-width="1.4" fill="none"/></svg></span></div>
</header>

<!-- hero -->
<h1 class="abs hero-title">Helping Small<br>Businesses Thrive<br>Ledger at a Time</h1>
<p class="abs lede" style="left:82px;top:451px;width:400px">Lorem ipsum dolor sit amet, consectetur adipiscing elit, sed do eiusmod tempor incididunt ut labore et dolore magna aliqua. Ut enim ad minim veniam, quis nostrud</p>
<div class="cta" style="left:82px;top:526px;width:228px">Book a free consultation
  <span class="cta-arrow"><svg width="18" height="18" viewBox="0 0 18 18"><path d="M4 14L14 4M6 4h8v8" stroke="#1d6f5b" stroke-width="1.4" fill="none"/></svg></span></div>

<div class="abs hero-photo" role="img" aria-label="Photo of a smiling woman in a grey blazer holding a tablet"></div>

<div class="abs tax-card">
  <div class="abs" style="left:15px;top:13px;width:28px;height:28px;border-radius:50%;background:var(--mint)"></div>
  <div class="abs" style="left:55px;top:22px;font-size:9px;font-weight:600;color:var(--ink)">CALCULATE TAX</div>
  <div class="abs" style="right:18px;top:15px;font-size:13px;color:#888">⋮</div>
  <div class="abs" style="left:0;width:279px;top:62px;text-align:center;font-size:29px;font-weight:500;color:var(--ink)">$276,00</div>
  <div class="abs" style="left:15px;top:126px;width:240px;height:6px;border-radius:3px;background:#dcdcdc"></div>
  <div class="abs" style="left:15px;top:126px;width:165px;height:6px;border-radius:3px;background:var(--teal)"></div>
  <div class="abs" style="left:174px;top:122px;width:13px;height:13px;border-radius:50%;background:#fff;border:1.5px solid var(--teal)"></div>
  <div class="abs" style="left:15px;top:147px;font-size:14px;font-weight:500;color:var(--ink)">$0,00</div>
  <div class="abs" style="right:24px;top:150px;font-size:14px;font-weight:500;color:var(--ink)">$1M</div>
</div>

<div class="partners">
  <span style="left:96px;font-size:20px"><i></i>Norvane</span>
  <span style="left:276px">Tarlo</span>
  <span style="left:440px;font-size:32px"><i></i>Brisken</span>
  <span style="left:708px;font-size:22px">Ostra</span>
  <span style="left:822px;font-size:24px"><i></i>Kelmar</span>
  <span style="left:1034px;font-size:15px">Pindle</span>
</div>

<!-- about -->
<div class="abs photo" role="img" aria-label="Business people reviewing charts on a tablet" style="left:94px;top:890px;width:422px;height:359px;background:linear-gradient(135deg,#1f2d52,#6f8fb8 55%,#cfdcea)"></div>
<h2 class="abs" style="left:545px;top:858px;font-size:36px;line-height:52px">Rooted In Accuracy Driven<br>By Your Success</h2>
<p class="abs lede" style="left:545px;top:986px;width:400px">Lorem ipsum dolor sit amet, consectetur adipiscing elit, sed do eiusmod tempor incididunt ut labore et dolore magna aliqua. Ut enim ad minim veniam, quis nostrud</p>

<div class="feature-icon" style="left:545px;top:1057px"><svg width="34" height="34" viewBox="0 0 34 34" fill="none" stroke="#1f3a33" stroke-width="1.4"><rect x="5" y="20" width="24" height="9"/><path d="M9 20v-7l6-4 5 4 6-6"/></svg></div>
<div class="feature-title" style="left:616px;top:1060px">Our Mission</div>
<div class="feature-text" style="left:616px;top:1083px">Our Mission Is To Simplify<br>Accounting For Business Owners</div>
<div class="abs" style="left:545px;top:1134px;width:258px;height:2px;background:var(--mint)"></div>
<div class="feature-icon" style="left:545px;top:1153px"><svg width="34" height="34" viewBox="0 0 34 34" fill="none" stroke="#1f3a33" stroke-width="1.4"><circle cx="17" cy="14" r="6"/><path d="M7 29c2-6 6-8 10-8s8 2 10 8"/></svg></div>
<div class="feature-title" style="left:616px;top:1157px">Our Vision</div>
<div class="feature-text" style="left:616px;top:1180px">Our Mission Is To Simplify<br>Accounting For Business Owners</div>
<div class="cta" style="left:545px;top:1238px;width:183px;height:42px;padding-left:43px;font-size:13.5px">Explore More
  <span class="cta-arrow" style="width:44px;height:44px"><svg width="18" height="18" viewBox="0 0 18 18"><path d="M4 14L14 4M6 4h8v8" stroke="#1d6f5b" stroke-width="1.4" fill="none"/></svg></span></div>
<div class="abs photo" role="img" aria-label="Team of colleagues working together at a laptop" style="left:859px;top:1071px;width:246px;height:209px;background:linear-gradient(135deg,#c9ccd1,#5e6c80 60%,#2e3a4c)"></div>

<!-- services -->
<div class="abs services-band"></div>
<div class="abs" role="img" aria-label="Woman working at a desk with computer and paperwork" style="left:98px;top:1418px;width:335px;height:378px;background:linear-gradient(150deg,#dfe6e1,#b8c5bd 45%,#f0f0f0)"></div>
<h2 class="abs" style="left:463px;top:1410px;font-size:37px;line-height:58px;font-weight:400">Smart Accounting Solutions for<br>Smarter Business Decisions</h2>
<p class="abs lede" style="left:463px;top:1551px;width:400px;color:#44504d">Lorem ipsum dolor sit amet, consectetur adipiscing elit, sed do eiusmod tempor incididunt ut labore et dolore magna aliqua. Ut enim ad minim veniam, quis nostrud</p>

<div class="service-card" style="left:330px"><div class="ico"><svg width="24" height="24" viewBox="0 0 24 24" fill="none" stroke="#1f3a33" stroke-width="1.3"><rect x="4" y="3" width="16" height="18"/><path d="M7 8h10M7 12h10M7 16h6"/></svg></div><h3>Accounting &nbsp;Bookkeeping</h3><p>Lorem ipsum dolor sit amet, consectetur adipiscing elit, sed do eiusmod tempor incididunt ut labore et</p></div>
<div class="service-card dark" style="left:591px"><div class="ico"><svg width="24" height="24" viewBox="0 0 24 24" fill="none" stroke="#1f3a33" stroke-width="1.3"><rect x="5" y="3" width="12" height="16"/><circle cx="16" cy="16" r="4"/></svg></div><h3>Payroll Management</h3><p>Lorem ipsum dolor sit amet, consectetur adipiscing elit, sed do eiusmod tempor incididunt ut labore et</p></div>
<div class="service-card" style="left:855px"><div class="ico"><svg width="24" height="24" viewBox="0 0 24 24" fill="none" stroke="#1f3a33" stroke-width="1.3"><circle cx="12" cy="9" r="4"/><path d="M4 21c1-5 4-7 8-7s7 2 8 7"/></svg></div><h3>Accounts Manage</h3><p>Lorem ipsum dolor sit amet, consectetur adipiscing elit, sed do eiusmod tempor incididunt ut labore et</p></div>

<div class="cta" style="left:98px;top:1813px;width:185px;height:42px;padding-left:48px;font-size:13.5px">Learn More
  <span class="cta-arrow" style="width:44px;height:44px"><svg width="18" height="18" viewBox="0 0 18 18"><path d="M4 14L14 4M6 4h8v8" stroke="#1d6f5b" stroke-width="1.4" fill="none"/></svg></span></div>

<!-- pricing -->
<h2 class="abs" style="left:113px;top:2006px;font-size:36px;line-height:58px">Simple Transparent<br>Pricing &nbsp;No Hidden Costs</h2>
<p class="abs lede" style="left:113px;top:2134px;width:400px">Lorem ipsum dolor sit amet, consectetur adipiscing elit, sed do eiusmod tempor incididunt ut labore et dolore magna aliqua. Ut enim ad minim veniam, quis nostrud</p>
<div class="plan-list">
  <div style="top:2205px">Bookkeeping Only</div>
  <div style="top:2246px">Bookkeeping + GST + Payroll</div>
  <div style="top:2287px">All Services + Advisory Support</div>
</div>
<div class="cta" style="left:113px;top:2334px;width:192px;height:41px;padding-left:34px;font-size:13.5px">Book A Free Call
  <span class="cta-arrow" style="width:43px;height:43px"><svg width="18" height="18" viewBox="0 0 18 18"><path d="M4 14L14 4M6 4h8v8" stroke="#1d6f5b" stroke-width="1.4" fill="none"/></svg></span></div>

<div class="plan" style="top:2006px">
  <div class="price">$199/<small>Month</small></div><div class="tier">Starter Plan</div>
  <div class="who">For Freelancers &amp; Solo<br>Business Owners<br>Includes</div>
  <ul><li>Tax Filing</li><li>Unlimited Support</li><li>Free Consultation</li><li>Ledgra Setup</li></ul>
</div>
<div class="plan-badge" style="left:996px;top:1989px">Basic</div>
<div class="plan" style="top:2224px">
  <div class="price">$199/<small>Month</small></div><div class="tier">Starter Plan</div>
  <div class="who">For Freelancers &amp; Solo<br>Business Owners<br>Includes</div>
  <ul><li>Tax Filing</li><li>Unlimited Support</li><li>Free Consultation</li><li>Ledgra Setup</li></ul>
</div>
<div class="plan-badge" style="left:986px;top:2208px">Standard</div>

<!-- faq -->
<h2 class="abs center" style="top:2490px;font-size:29px">FAQs</h2>
<h2 class="abs center" style="top:2534px;font-size:37px;font-weight:400">Your Questions, Clearly Answered</h2>
<div class="rule" style="top:2607px"></div>
<div class="abs center" style="top:2622px;font-size:18px;color:var(--ink)">How Do I Get Started With A Project?</div>
<div class="rule" style="top:2656px"></div>
<div class="abs center" style="top:2680px;font-size:15px;line-height:25px;color:#8a9290">Yes. We Have Extensive Experience Delivering<br>Projects For Local Councils</div>
<div class="abs" style="left:384px;top:2748px;width:432px;height:65px;background:var(--mint-soft);border-radius:4px;text-align:center;line-height:65px;font-size:18px;color:var(--ink)">What Industries Do You Serve?</div>
<p class="abs center" style="top:2836px;font-size:11.5px;line-height:19.5px;color:#6a7270">Lorem ipsum dolor sit amet, consectetur adipiscing elit, sed do eiusmod tempor<br>incididunt ut labore et dolore magna aliqua. Ut enim ad minim veniam, quis nostrud<br>exercitation ullamco Lorem ipsum dolor sit amet, consectetur adipiscing elit, sed do<br>eiusmod tempor incididunt ut labore et dolore magna</p>

<!-- contact -->
<div class="abs form-panel"></div>
<div class="field-label" style="left:276px;top:3058px">Name</div>
<div class="field" style="left:276px;top:3078px;width:169px;height:27px"></div>
<div class="field-label" style="left:455px;top:3058px">Phone</div>
<div class="field" style="left:455px;top:3078px;width:170px;height:27px"></div>
<div class="field-label" style="left:276px;top:3128px">Email</div>
<div class="field" style="left:276px;top:3147px;width:349px;height:28px"></div>
<div class="field-label" style="left:276px;top:3197px">Adress</div>
<div class="field" style="left:276px;top:3217px;width:349px;height:28px"></div>
<div class="field-label" style="left:276px;top:3256px">Message</div>
<div class="field" style="left:276px;top:3276px;width:349px;height:84px"></div>
<div class="abs" style="left:276px;top:3396px;width:349px;height:36px;border-radius:18px;background:var(--mint);text-align:center;line-height:36px;font-size:14px;font-weight:500;color:var(--ink)">Submit</div>

<div class="abs info-panel">
  <div class="abs" style="left:19px;top:90px;font-family:'Lexend',sans-serif;font-size:18px;color:#fff">info</div>
  <div class="row" style="top:151px"><svg width="16" height="16" viewBox="0 0 16 16" fill="none" stroke="#fff" stroke-width="1.2"><path d="M3 2h3l1 3-2 1.5a8 8 0 004 4L10.5 9l3 1v3a1.5 1.5 0 01-1.5 1.5A11 11 0 011.5 3.5 1.5 1.5 0 013 2z"/></svg>(021) 480-3316</div>
  <div class="row" style="top:207px"><svg width="16" height="16" viewBox="0 0 16 16" fill="none" stroke="#fff" stroke-width="1.2"><rect x="1.5" y="3" width="13" height="10"/><path d="M1.5 3l6.5 6 6.5-6"/></svg>studio@vellart.co.nz</div>
  <div class="row" style="top:263px"><svg width="16" height="16" viewBox="0 0 16 16" fill="none" stroke="#fff" stroke-width="1.2"><path d="M8 15s5-5 5-9A5 5 0 003 6c0 4 5 9 5 9z"/><circle cx="8" cy="6" r="1.8"/></svg>18 Harbour Lane, Tauranga</div>
  <div class="row" style="top:316px;font-size:11px;gap:22px">Social Media <span style="display:flex;gap:5px"><i style="width:9px;height:9px;background:#fff;display:block"></i><i style="width:9px;height:9px;background:#fff;display:block"></i><i style="width:9px;height:9px;background:#fff;display:block"></i><i style="width:9px;height:9px;border-radius:50%;background:#fff;display:block"></i></span></div>
</div>

<!-- footer -->
<footer class="abs site-footer">
  <div class="abs" style="left:125px;top:205px;display:flex;align-items:center;gap:10px;font-family:'Lexend',sans-serif;font-weight:500;font-size:29px;letter-spacing:5px;color:#fff"><span style="width:20px;height:20px;border-radius:50%;background:#fff"></span>VELLART</div>
  <a style="left:447px;top:75px">Home</a>
  <a style="left:447px;top:116px">About Us</a>
  <a style="left:447px;top:158px">Services</a>
  <a style="left:447px;top:201px">Pricing</a>
  <a style="left:447px;top:244px">Faqs</a>
  <a style="left:590px;top:73px">Blog</a>
  <a style="left:590px;top:105px">Contact Us</a>
  <a style="left:590px;top:138px">Faqs</a>
  <a style="left:590px;top:170px">Privacy Policy</a>
  <a style="left:590px;top:201px">Terms And Condition</a>
  <div class="f" style="left:816px;top:74px;font-family:'Lexend',sans-serif;font-size:18px">info</div>
  <div class="f" style="left:818px;top:118px;display:flex;gap:8px;align-items:center;font-size:13px"><svg width="14" height="14" viewBox="0 0 16 16" fill="none" stroke="#fff" stroke-width="1.3"><path d="M8 15s5-5 5-9A5 5 0 003 6c0 4 5 9 5 9z"/><circle cx="8" cy="6" r="1.8"/></svg>18 Harbour Lane, Tauranga 3110</div>
  <div class="f" style="left:818px;top:155px;display:flex;gap:8px;align-items:center;font-size:13px"><svg width="14" height="14" viewBox="0 0 16 16" fill="none" stroke="#fff" stroke-width="1.3"><path d="M3 2h3l1 3-2 1.5a8 8 0 004 4L10.5 9l3 1v3a1.5 1.5 0 01-1.5 1.5A11 11 0 011.5 3.5 1.5 1.5 0 013 2z"/></svg>021-774-2093</div>
  <div class="f" style="left:818px;top:191px;display:flex;gap:8px;align-items:center;font-size:13px"><svg width="14" height="14" viewBox="0 0 16 16" fill="none" stroke="#fff" stroke-width="1.3"><rect x="1.5" y="3" width="13" height="10"/><path d="M1.5 3l6.5 6 6.5-6"/></svg>hello@vellart.co.nz</div>
  <div class="foot-rule" style="top:318px"></div>
  <div class="f" style="left:0;width:1200px;text-align:center;top:340px;font-size:11px;font-weight:600">Copyright © 2025. All Rights Reserved.</div>
  <div class="foot-rule" style="top:380px"></div>
</footer>

</body>
</html>
```